Business Card Design Project

We need a Business Card for an Mechanical Engineering firm in Singapore. The design should be Modern & Technical looking, yet eye catching.

Our company deals in Cutting Tools & Machine Accessories for the Manufacturing Industries such as Oil & Gas, Aero Space, etc... For more information on our Company, you can either email me or view our website www.valtrion.com.sg.

We are trying to revamp our image to give our consumers a fresh new perspective to our company, so we welcome all ideas.

Industry/Entity Type

Business

Requirements
Must have
• Must incorporate New Company Logo into the card as shown in Uploaded file.

```html
<!DOCTYPE html>
<html lang="en">
<head>
<meta charset="utf-8">
<title>Valtrion Tools – Business Card</title>
<link rel="stylesheet" href="https://fonts.googleapis.com/css2?family=Arimo:wght@400;700&display=swap">
<style>
  :root {
    --card-white: #ffffff;
    --brand-maroon: #8c0b33;
    --brand-dark: #3b0a1c;
    --ink: #111111;
    --steel-light: #dfe6e2;
    --steel-mid: #9fb3aa;
    --steel-dark: #5f746c;
    --steel-rose: #b89aa8;
  }
  html, body {
    margin: 0;
    padding: 0;
    width: 1200px;
    height: 695px;
    overflow: hidden;
    background: var(--card-white);
  }
  .card {
    position: relative;
    width: 1200px;
    height: 695px;
    background: var(--card-white);
    font-family: "Arimo", Arial, sans-serif;
    color: var(--ink);
    overflow: hidden;
  }
  .tool-strip {
    position: absolute;
    top: 0;
    height: 605px;
  }
  .tool-strip--left {
    left: 0;
    width: 345px;
    background: linear-gradient(160deg, var(--steel-light) 0%, var(--steel-mid) 35%, var(--steel-rose) 55%, var(--steel-mid) 75%, var(--steel-light) 100%);
  }
  .tool-strip--right {
    right: 0;
    width: 135px;
    background: linear-gradient(90deg, var(--steel-light) 0%, var(--steel-mid) 50%, var(--steel-dark) 100%);
  }
  .contact {
    position: absolute;
    left: 379px;
    top: 62px;
  }
  .contact__name {
    margin: 0;
    font-size: 45px;
    font-weight: 400;
    line-height: 1.1;
  }
  .contact__title {
    margin: 4px 0 0;
    font-size: 34px;
    font-weight: 400;
    line-height: 1.1;
  }
  .contact__address {
    margin: 28px 0 0;
    font-style: normal;
    font-size: 27px;
    line-height: 41px;
  }
  .contact__web {
    display: block;
    font-size: 22px;
    line-height: 30px;
  }
  .brand-mark {
    position: absolute;
    left: 760px;
    top: 300px;
  }
  .brand-name {
    position: absolute;
    left: 379px;
    top: 512px;
    margin: 0;
    font-size: 66px;
    font-weight: 400;
    line-height: 1;
    color: var(--brand-dark);
    white-space: nowrap;
  }
  .base-band {
    position: absolute;
    left: 0;
    bottom: 0;
    width: 1200px;
    height: 90px;
    background: var(--brand-maroon);
  }
</style>
</head>
<body>
<div class="card">
  <div class="tool-strip tool-strip--left" role="img" aria-label="Close-up photograph of twisted steel drill bits"></div>
  <div class="tool-strip tool-strip--right" role="img" aria-label="Close-up photograph of stacked steel machine parts"></div>

  <section class="contact">
    <h1 class="contact__name">Employee Name</h1>
    <p class="contact__title">Title</p>
    <address class="contact__address">
      27 Kallang Way, #03-12<br>
      Meridian Trade Centre,<br>
      Singapore 349281<br>
      <span class="contact__web">www.valtrion.com.sg</span>
    </address>
  </section>

  <svg class="brand-mark" width="160" height="160" viewBox="0 0 160 160" aria-hidden="true">
    <circle cx="80" cy="80" r="78" fill="#8c0b33"/>
  </svg>
  <p class="brand-name">VALTRION TOOLS</p>

  <div class="base-band"></div>
</div>
</body>
</html>
```